Make Edits to Website You Already Created

You created the design for my website (Quick Page Forge) which is now PageLoomly.com. I need you to modify the HTML as follows:
1. Temporarily host it on a server with a URL I can view the live site while you develop and make changes as I work with you through perfecting it. Once all changes are made and the site looks and functions perfectly, I will deploy the code on my server and it will become the new face of PageLoomly.com.
2. I have 3 MP4 videos that I would like to replace the hero image you originally provided. The videos should each run for approximately 6-8 seconds, then scroll to the next video.
3. All the content (text) in the website you created is filler text. I need you to replace it with the actual content that currently shows on PageLoomly.com. I realize the layout of your template is much different than the current PageLoomly page. However, do your best to utilize the content from the existing site without changing the layout or format that you created. If there are any sections of your template that you can't find text from the current site to put there, let me know and I will come up with more content to fill all the sections.
4. I need four additional pages (sub-pages) created for the following topics:
a. About PageLoomly
b. Learn More About AI
c. The History of AI
d. Make Money with GPT
*I will provide the content for these new pages if you come up with the design/layout.
5. Once everything has been edited to my satisfaction and working properly, provide the full Bootstrap HTML code for me to easily deploy on my server and replace the existing PageLoomly.com website.
I have attached the original HTML files you provided when you created the design and the videos for the hero slider.
Let me know what else you need from me.
Thanks!

```html
<!DOCTYPE html>
<html lang="en">
<head>
<meta charset="UTF-8">
<title>PageLoomly – Privacy Policy</title>
<link href="https://fonts.googleapis.com/css2?family=Poppins:wght@300;400;500;600;700&display=swap" rel="stylesheet">
<style>
:root{
  --navy:#0b1632;
  --navy-2:#111d3d;
  --ink:#1b1f2a;
  --body:#3d4250;
  --muted:#9aa3b8;
  --white:#ffffff;
  --line:#26335a;
}
*{margin:0;padding:0;box-sizing:border-box}
html,body{width:710px;height:1200px;overflow:hidden;background:var(--white)}
body{font-family:"Poppins",sans-serif;color:var(--body);position:relative}

.site-header{height:52px;background:var(--navy);display:flex;align-items:center;justify-content:space-between;padding:0 38px}
.brand{display:flex;align-items:center;gap:7px;color:var(--white);font-weight:600;font-size:17px}
.brand-dot{width:16px;height:16px;border-radius:50%;background:var(--white)}
.main-nav{display:flex;gap:26px}
.main-nav a{color:var(--white);text-decoration:none;font-size:8.5px;font-weight:400}

.policy{padding:36px 38px 0 38px;height:1025px}
.policy-title{font-size:29px;font-weight:300;color:var(--ink);margin-bottom:30px;letter-spacing:-.3px}
.policy-title strong{font-weight:700}
.policy-section{margin-bottom:26px}
.policy-section h2{font-size:8.6px;font-weight:600;color:var(--ink);margin-bottom:9px}
.policy-section p,.policy-section li{font-size:8.6px;line-height:13px;color:var(--body);max-width:620px}
.policy-section ul{list-style:none;padding-left:10px}
.policy-section li::before{content:"•";margin-right:6px}

.site-footer{position:absolute;left:0;right:0;top:1077px;height:123px;background:var(--navy);padding:26px 38px 0 38px;color:var(--white)}
.footer-grid{display:flex;justify-content:space-between}
.footer-about{width:170px}
.footer-about .brand{font-size:18px;margin-bottom:8px}
.footer-about p{font-size:6px;line-height:9px;color:var(--muted)}
.footer-col h3{font-size:8.5px;font-weight:600;margin-bottom:7px}
.footer-col a{display:block;color:var(--white);text-decoration:none;font-size:6.8px;line-height:12px}
.footer-col.nav{margin-left:60px}
.social-grid{display:grid;grid-template-columns:repeat(5,16px);gap:6px}
.social-grid span{width:16px;height:16px;border-radius:50%;border:1px solid var(--white)}
.copyright{position:absolute;left:38px;bottom:10px;font-size:6px;color:var(--muted)}
</style>
</head>
<body>
<header class="site-header">
  <div class="brand"><span class="brand-dot"></span>PageLoomly</div>
  <nav class="main-nav">
    <a href="#">About PageLoomly</a>
    <a href="#">Learn More About AI</a>
    <a href="#">The History of AI</a>
    <a href="#">Make Money with GPT</a>
  </nav>
</header>

<main class="policy">
  <h1 class="policy-title">Our Privacy <strong>Policy</strong></h1>

  <section class="policy-section">
    <h2>1. Introduction</h2>
    <p>Welcome to PageLoomly.com. Your privacy is of utmost importance to us. This Privacy Policy is intended to help you understand what information we collect, how we use it, and what choices you have.</p>
  </section>

  <section class="policy-section">
    <h2>2. Information We Collect</h2>
    <p>2.1 Direct Information: When you sign up for our services, we collect personal information that includes your name, email address, phone number, and other necessary details to help you create and manage your website.</p>
    <p>2.2 Automated Information: We use cookies and other tracking technologies to collect information about how you use PageLoomly.com, including your IP address, browser type, device type, and other relevant data.</p>
  </section>

  <section class="policy-section">
    <h2>3. How We Use Your Information</h2>
    <p>We use the collected information for various purposes, such as:</p>
    <ul>
      <li>To provide, maintain, and improve our services.</li>
      <li>To communicate with you, including sending notifications and promotional offers.</li>
      <li>To monitor and analyze usage and trends.</li>
      <li>To enhance security and ensure a safe user experience.</li>
    </ul>
  </section>

  <section class="policy-section">
    <h2>4. Communications Policy</h2>
    <p>By using PageLoomly.com, you agree to allow us to communicate with you via any email address or phone number you provide while using our platform. All communication messages will include an opt-out option, which when selected, will terminate any future communication from PageLoomly.</p>
  </section>

  <section class="policy-section">
    <h2>5. Information Sharing and Disclosure</h2>
    <p>Your personal information will not be sold or shared with third parties without your consent, except:</p>
    <ul>
      <li>To comply with legal obligations.</li>
      <li>To protect our rights, privacy, safety, or property and that of our users or the public.</li>
    </ul>
  </section>

  <section class="policy-section">
    <h2>6. Security</h2>
    <p>We implement strict security measures to protect your personal information. However, no method of transmission or electronic storage is 100% secure. We strive to protect your data but cannot guarantee its absolute security.</p>
  </section>

  <section class="policy-section">
    <h2>7. User Choices and Control</h2>
    <p>You have the right to:</p>
    <ul>
      <li>Access, correct, update, or request the deletion of your personal data.</li>
      <li>Opt-out of being contacted by us for marketing or promotional purposes.</li>
      <li>Decide if you wish to receive notifications or newsletters.</li>
    </ul>
  </section>

  <section class="policy-section">
    <h2>8. Children's Privacy</h2>
    <p>PageLoomly.com is not designed for individuals under the age of 13. We do not intentionally gather personal information from visitors under the age of 13. If you believe we might have information from a child under 13, please contact us, and we will take necessary actions to remove that information.</p>
  </section>

  <section class="policy-section">
    <h2>9. Changes to this Policy</h2>
    <p>We reserve the right to modify this Privacy Policy at any time. Any changes will be effective immediately upon posting. We advise reviewing our Privacy Policy regularly.</p>
  </section>

  <section class="policy-section">
    <h2>10. Contact Us</h2>
    <p>If you have questions about this Privacy Policy or our practices, please CONTACT US.</p>
    <p>By using PageLoomly.com, you agree to the practices described in this Privacy Policy.</p>
  </section>
</main>

<footer class="site-footer">
  <div class="footer-grid">
    <div class="footer-about">
      <div class="brand"><span class="brand-dot"></span>PageLoomly</div>
      <p>Build fast, polished websites with smart AI tools that write, design and launch pages for your business in minutes.</p>
    </div>
    <div class="footer-col nav">
      <h3>Navigation</h3>
      <a href="#">About PageLoomly</a>
      <a href="#">Learn More About AI</a>
      <a href="#">The History of AI</a>
      <a href="#">Make Money with GPT</a>
    </div>
    <div class="footer-col">
      <h3>Links</h3>
      <a href="#">Terms &amp; Condition</a>
      <a href="#">FAQ</a>
      <a href="#">Privacy Policy</a>
      <a href="#">Contact Us</a>
    </div>
    <div class="footer-col">
      <h3>Follow Us</h3>
      <div class="social-grid" aria-label="Social links">
        <span></span><span></span><span></span><span></span><span></span>
        <span></span><span></span><span></span><span></span><span></span>
      </div>
    </div>
  </div>
  <p class="copyright">© 2023 PageLoomly. All Rights Reserved.</p>
</footer>
</body>
</html>
```